SUMMIT GATHERING 2021. August 20th -22nd.

The Hosts of the conference: Grace Tabernacle-Pastors Ron n Della ( Picture with two persons)

Guest Minister: Bishop Lucinda Okotieno. (Cedar Ridge Awakening)

Venue:
Sealand Gateway Lodgeview. 4817 North 239th Avenue Seattle, WA 98174.

Conference times.
Friday August 20th 6pm-8:30pm
Saturday August 21st. 6pm-8:30pm

Sunday August 22nd 10am-1pm
“ CHURCH RENEWAL GATHERING”

5pm-7:30pm
TWOFOLD SURGE GATHERING.

Target Market(s)

18-55

Industry/Entity Type

Religious/ Entertainment.

Requirements
Must have
• A highlight of the Relaunch service on Sunday August 22nd 5pm-7:30pm.
Nice to have
• Excellent ideas….

```html
<!DOCTYPE html>
<html lang="en">
<head>
<meta charset="utf-8">
<title>Summit Gathering 2021</title>
<link rel="stylesheet" href="https://fonts.googleapis.com/css2?family=Montserrat:ital,wght@0,300;0,400;0,600;0,700;0,800;1,800&display=swap">
<style>
  :root {
    --page-bg: #e9e9e9;
    --poster-bg: #232323;
    --white: #ffffff;
    --soft-white: #e6e6e6;
    --gold: #d6a55a;
    --gold-light: #f2d9a8;
    --gold-dark: #b07c35;
    --ink: #1c1c1c;
  }
  * { margin: 0; padding: 0; box-sizing: border-box; }
  html, body { width: 1200px; height: 900px; overflow: hidden; }
  body {
    background: var(--page-bg);
    font-family: "Montserrat", Arial, sans-serif;
    color: var(--white);
    position: relative;
  }
  .poster {
    position: absolute;
    left: 294px; top: 20px;
    width: 612px; height: 860px;
    background: var(--poster-bg);
    overflow: hidden;
  }
  .poster > * { position: absolute; }

  .brand-mark {
    left: 62px; top: 118px; width: 112px;
    display: flex; flex-direction: column; align-items: center; gap: 8px;
  }
  .brand-mark .square { width: 40px; height: 40px; background: var(--gold); }
  .brand-mark .name {
    font-weight: 700; font-size: 13px; color: var(--gold);
    text-align: center; line-height: 1.2; text-transform: uppercase; letter-spacing: 0.5px;
  }

  .title-top { left: 183px; top: 52px; font-weight: 300; font-size: 58px; line-height: 1; letter-spacing: 1px; }
  .title-main {
    left: 181px; top: 104px; font-weight: 800; font-size: 52px; line-height: 1; letter-spacing: -0.5px;
    background: linear-gradient(90deg, var(--gold-dark), var(--gold) 55%, var(--gold-light));
    -webkit-background-clip: text; background-clip: text; color: transparent;
  }
  .title-year { left: 183px; top: 154px; font-weight: 400; font-size: 48px; line-height: 1; }
  .title-dates { left: 300px; top: 156px; font-weight: 800; font-style: italic; font-size: 14px; color: var(--gold); }

  .guest-photo {
    left: 70px; top: 222px; width: 183px; height: 189px;
    background: radial-gradient(ellipse at 50% 35%, #9a9a9a, #4a4a4a 70%, #2e2e2e);
    border-radius: 90px 90px 0 0;
  }
  .guest-info { left: 245px; top: 260px; line-height: 1.35; }
  .guest-info .label { font-size: 11px; font-weight: 400; color: var(--soft-white); }
  .guest-info .name { font-size: 13.5px; font-weight: 700; }
  .guest-info .note { font-size: 10px; font-weight: 400; color: var(--soft-white); }

  .rule { height: 1.5px; background: var(--gold); }
  .rule::before {
    content: ""; position: absolute; left: -3px; top: -3px;
    width: 7px; height: 7px; border-radius: 50%; background: var(--gold);
  }
  .rule-upper { left: 49px; top: 411px; width: 366px; }
  .rule-lower { left: 49px; top: 679px; width: 563px; }

  .hosts-photo {
    left: 414px; top: 306px; width: 198px; height: 373px;
    background: linear-gradient(160deg, #8c8c8c, #5a5a5a 45%, #bcbcbc 80%, #9a9a9a);
    border-radius: 80px 80px 0 0;
  }

  .details { left: 70px; top: 432px; width: 330px; }
  .details .label { font-size: 11px; font-weight: 400; color: var(--soft-white); text-transform: uppercase; margin-bottom: 3px; }
  .details .value { font-size: 13.5px; font-weight: 700; line-height: 1.3; }
  .details .venue { margin-bottom: 20px; }
  .details .session { margin-top: 7px; }

  .highlight { left: 70px; top: 694px; }
  .highlight .heading {
    font-weight: 800; font-style: italic; font-size: 19.5px; line-height: 1.1;
    text-transform: uppercase; letter-spacing: -0.3px; color: var(--gold);
  }
  .highlight .time { font-size: 13.5px; font-weight: 700; margin-top: 6px; }

  .hosts-info { left: 415px; top: 697px; line-height: 1.3; }
  .hosts-info .label { font-size: 11px; font-weight: 400; color: var(--soft-white); text-transform: uppercase; }
  .hosts-info .name { font-size: 13.5px; font-weight: 700; margin-top: 1px; }

  .banner { left: 278px; top: 794px; width: 334px; height: 34px; }
  .banner svg { position: absolute; inset: 0; }
  .banner .text {
    position: absolute; left: 14px; top: 0; height: 34px; line-height: 34px;
    font-weight: 800; font-style: italic; font-size: 16.5px; letter-spacing: -0.2px;
    color: var(--ink); text-transform: uppercase; white-space: nowrap;
  }
</style>
</head>
<body>
  <main class="poster">
    <div class="brand-mark">
      <span class="square"></span>
      <span class="name">Grace Tabernacle</span>
    </div>

    <h1 class="title-top">SUMMIT</h1>
    <div class="title-main">GATHERING</div>
    <div class="title-year">2021</div>
    <div class="title-dates">August 20th -22nd</div>

    <div class="guest-photo" role="img" aria-label="Portrait of guest minister Bishop Lucinda Okotieno"></div>
    <div class="guest-info">
      <div class="label">Guest Minister:</div>
      <div class="name">Bishop Lucinda Okotieno</div>
      <div class="note">(Cedar Ridge Awakening)</div>
    </div>

    <div class="rule rule-upper"></div>

    <div class="hosts-photo" role="img" aria-label="Photo of hosts Pastors Ron and Della"></div>

    <section class="details">
      <div class="venue">
        <div class="label">Venue:</div>
        <div class="value">Sealand Gateway Lodgeview.<br>4817 North 239th, Avenue Seattle,<br>WA 98174</div>
      </div>
      <div class="label">Conference Times:</div>
      <div class="session value">Friday August 20th<br>6pm-8:30pm</div>
      <div class="session value">Saturday August 21st<br>6pm-8:30pm</div>
      <div class="session value">Sunday August 22nd<br>10am-1pm</div>
    </section>

    <div class="rule rule-lower"></div>

    <div class="highlight">
      <div class="heading">Church<br>Renewal Gathering</div>
      <div class="time">5pm-7:30pm</div>
    </div>

    <div class="hosts-info">
      <div class="label">The hosts of the<br>conference:</div>
      <div class="name">Grace Tabernacle-<br>Pastors Ron n Della</div>
    </div>

    <div class="banner">
      <svg width="334" height="34" viewBox="0 0 334 34" aria-hidden="true">
        <defs>
          <linearGradient id="banner-gold" x1="0" x2="1" y1="0" y2="0">
            <stop offset="0" stop-color="#c9934a"/>
            <stop offset="0.6" stop-color="#d9aa62"/>
            <stop offset="1" stop-color="#f3dcaf"/>
          </linearGradient>
        </defs>
        <polygon points="7,0 334,0 334,34 0,34" fill="url(#banner-gold)"/>
      </svg>
      <span class="text">Twofold Surge Gathering</span>
    </div>
  </main>
</body>
</html>
```